Orlent Telecom Business Card Competition

High quality international communications for consumers and business. We are re-designing our website and re-branding. Our current (old) website can be viewed at www.goorlent-example.net Vision statement - We enable people and communities to build and maintain strong and lasting global connections This is the brand image that we are trying to get across: •Quality—Orlent delivers the highest quality connections wherever you need to communicate. •Service—Orlent is always there for you, with the industry-leading service that promises to ensure that every experience is a good one. •Value—Orlent provides the best value in the global communications market. Typical messaging: Connecting the Most Important People in the World. Focus on international communications

We want to convey our service quality and that we really care about the service we provide and our customers. We want to emphasis the international aspect of our business. We want to make it personal, but it has to relate to business as well as individuals. We want the card to be unique in design but clear enough to read. We want a business prospect as well as a regular person to look at our card and know what we do.

Target Market(s)

Consumer - multi-ethnic consumer base living in the US calling, texting and connecting with family and friends in countries around the world 2. Busine

Industry/Entity Type

Communications

Requirements
Must have
• 1. Logo must be visible (see uploaded)

2.Artist can use variations of our company colors to accent our logo:

Hex Codes:
Magenta = ab3179
Blue = 2895c0
Green = 8ebb3f

3.Must have the following slogan visible: Because Clear Calls Matter

below are the required data fields:

Full Name: Mark Tallow
Position: Chief Financial Officer
Office: +1 608-441-2871 ext.318
Mobile: +1 608-441-2871
Fax: +1 608-441-2871
Email: MarkT@goorlent-example.net
URL: www.goorlent-example.net
Address:
71820 Brindle Avenue
suite 412
Harlow Bay, WI 53718
USA

Nice to have
• Die cut cards or uniquely shaped cards would be interesting to see but not required

```html
<!DOCTYPE html>
<html lang="en">
<head>
<meta charset="utf-8">
<title>Orlent Telecom – Business Card</title>
<link rel="stylesheet" href="https://fonts.googleapis.com/css2?family=Arimo:wght@400;700&display=swap">
<style>
  :root {
    --magenta: #ab3179;
    --blue: #2895c0;
    --green: #8ebb3f;
    --paper: #f4f4f4;
    --charcoal: #3a3a3a;
    --ink: #2b2b2b;
    --grey: #8a8a8a;
    --backdrop: #b9b9b9;
  }
  * { box-sizing: border-box; margin: 0; padding: 0; }
  html, body { width: 1200px; height: 880px; overflow: hidden; }
  body {
    background: var(--backdrop);
    font-family: "Arimo", Arial, sans-serif;
    position: relative;
  }
  .card {
    position: absolute;
    left: 250px;
    width: 700px;
    height: 400px;
    border-radius: 28px;
    overflow: hidden;
  }
  .card--front { top: 20px; background: var(--paper); color: var(--ink); }
  .card--back { top: 460px; background: var(--charcoal); }

  /* Front */
  .front-brand {
    position: absolute;
    left: 60px; top: 40px;
    width: 90px; height: 320px;
    display: flex;
    flex-direction: column;
    align-items: center;
    justify-content: center;
    gap: 16px;
  }
  .front-brand__name {
    writing-mode: vertical-rl;
    transform: rotate(180deg);
    font-size: 34px;
    font-weight: 700;
    color: var(--magenta);
    letter-spacing: 2px;
    white-space: nowrap;
  }
  .brand-square {
    flex: 0 0 auto;
    display: block;
    width: 26px; height: 26px;
    background: var(--blue);
    border-radius: 6px;
  }
  .contact {
    position: absolute;
    left: 245px; top: 50px;
    right: 30px;
  }
  .contact__name {
    font-size: 30px;
    text-transform: uppercase;
    letter-spacing: 0.5px;
  }
  .contact__title { font-size: 18px; font-weight: 700; margin-top: 4px; }
  .contact__rule { display: block; margin: 10px 0 14px; width: 330px; height: 7px; }
  .contact__list { list-style: none; font-size: 19px; line-height: 25px; }
  .contact__label { display: inline-block; width: 26px; font-size: 16px; }
  .label--t { color: var(--blue); }
  .label--m { color: var(--magenta); }
  .label--f { color: var(--green); }
  .label--e { color: var(--grey); }
  .contact__address { font-size: 19px; line-height: 25px; margin-top: 16px; }
  .contact__url { font-size: 19px; margin-top: 26px; }
  .contact__url strong { color: var(--blue); }

  /* Back */
  .back-brand {
    position: absolute;
    left: 0; right: 0; top: 95px;
    display: flex;
    align-items: center;
    justify-content: center;
    gap: 22px;
  }
  .back-brand .brand-square { width: 54px; height: 54px; border-radius: 12px; }
  .back-brand__name {
    font-size: 64px;
    font-weight: 700;
    color: #ffffff;
    letter-spacing: 2px;
  }
  .slogan-band {
    position: absolute;
    left: 70px; right: 70px; top: 250px;
    height: 46px;
    background: var(--magenta);
    border-radius: 6px;
    display: flex;
    align-items: center;
    justify-content: center;
    font-size: 24px;
    color: #2e2e2e;
  }
</style>
</head>
<body>
  <section class="card card--front" aria-label="Card front">
    <div class="front-brand">
      <span class="brand-square"></span>
      <span class="front-brand__name">Orlent Telecom</span>
    </div>
    <div class="contact">
      <h1 class="contact__name">Mark Tallow</h1>
      <p class="contact__title">Chief Financial Officer</p>
      <svg class="contact__rule" viewBox="0 0 330 7" aria-hidden="true">
        <line x1="0" y1="1" x2="330" y2="1" stroke="#2895c0" stroke-width="1.4"/>
        <line x1="0" y1="3.5" x2="330" y2="3.5" stroke="#ab3179" stroke-width="1.4"/>
        <line x1="0" y1="6" x2="330" y2="6" stroke="#8ebb3f" stroke-width="1.4"/>
      </svg>
      <ul class="contact__list">
        <li><span class="contact__label label--t">T</span>+1 608-441-2871 ext.318</li>
        <li><span class="contact__label label--m">M</span>+1 608-441-2871</li>
        <li><span class="contact__label label--f">F</span>+1 608-441-2871</li>
        <li><span class="contact__label label--e">E</span>MarkT@goorlent-example.net</li>
      </ul>
      <p class="contact__address">71820 Brindle Avenue, suite 412<br>Harlow Bay, WI 53718 USA</p>
      <p class="contact__url">www.<strong>goorlent-example</strong>.net</p>
    </div>
  </section>

  <section class="card card--back" aria-label="Card back">
    <div class="back-brand">
      <span class="brand-square"></span>
      <span class="back-brand__name">Orlent Telecom</span>
    </div>
    <div class="slogan-band">Because Clear Calls Matter</div>
  </section>
</body>
</html>
```